Catalog for Lumiveso

Hi, we are a new school That Teach arabic language in Tunisia, we are looking to a catalog conceptulize That describe all details of our activity and what we offer. An example of a catalog is attached to this brifs. Please make something basing on it. What we like about this catalog it the Police and the fact That Each page contenir pictures with "some text", it is not stuffed with Paragraphs and That What Makes it clear Vous pouvez aussi find a description of all sections That We want to privide our with catalog. (Name of pictures is related to the word section in the table). Vous pouvez aussi find two .zip files, Tunis pictures contains pictures related to the town and the second one contains students picture. Accomodation and school pictures still missing, the Provided wil be soon. Texts Will Be Provided soon, Meanwhile, work your magic on the design! Waiting for your suggestions! Thank u.

```html
<!DOCTYPE html>
<html lang="en">
<head>
<meta charset="utf-8">
<title>Lumiveso Catalog</title>
<link href="https://fonts.googleapis.com/css2?family=Roboto+Condensed:wght@300;400;700&display=swap" rel="stylesheet">
<style>
:root{
  --bg:#e6e6e6;
  --paper:#ffffff;
  --ink:#1a1a1a;
  --muted:#444;
  --rule:#8a8a8a;
  --blue:#1ea3ea;
  --magenta:#ec008c;
  --yellow:#fff200;
  --night-top:#0c1f66;
  --night-mid:#2a3f8a;
  --glow:#e8a93a;
  --sand:#c9a77a;
  --sky:#5b95d6;
  --white-town:#e9eef3;
  --sea:#6f9fc0;
  --map:#eceeea;
}
*{box-sizing:border-box;margin:0;padding:0}
html,body{width:1200px;height:778px;overflow:hidden;background:var(--bg)}
body{font-family:"Roboto Condensed",Arial Narrow,sans-serif;color:var(--ink);position:relative}
.page{position:absolute;background:var(--paper);overflow:hidden}
.row-top{top:18px;height:366px}
.row-bottom{top:395px;height:367px}
.p1{left:20px;width:282px}.p2{left:314px;width:283px}.p3{left:608px;width:282px}.p4{left:902px;width:283px}
.p5{left:20px;width:285px}.p6{left:315px;width:283px}.p7{left:608px;width:282px}.p8{left:900px;width:285px}
.abs{position:absolute}
.photo{position:absolute}
.night{background:linear-gradient(180deg,var(--night-top) 0%,var(--night-mid) 40%,#6a5a4a 65%,var(--glow) 85%,#7a4a20 100%)}
.church{background:linear-gradient(180deg,var(--sky) 0%,#a9c4e4 25%,#e2cfa0 55%,var(--sand) 100%)}
.whitetown{background:linear-gradient(180deg,#8fb7e2 0%,var(--white-town) 40%,#d8dde2 75%,#7f9a6a 100%)}
.ruins{background:linear-gradient(180deg,#e8edf2 0%,#c79a6e 40%,#9c6a42 100%)}
.harbour{background:linear-gradient(180deg,#d8e4ef 0%,#b8c8d6 50%,var(--sea) 65%,#3f6d92 100%)}
.roofs{background:linear-gradient(180deg,#9cc0e6 0%,#e6e2d8 40%,#c9b48e 75%,#8e7a5c 100%)}
.waterfall{background:linear-gradient(180deg,#3d5a2a 0%,#a88a5e 35%,#6a8a6a 65%,#2f9a8a 100%)}
.folio{font-size:7px;position:absolute}
.small{font-size:6px;line-height:1.45;color:var(--muted)}
.bold{font-weight:700;color:var(--ink)}
/* contents */
.contents-title{left:16px;top:24px;font-size:46px;font-weight:300;letter-spacing:-.5px}
.toc{position:absolute;top:88px;width:122px}
.toc.left{left:16px}.toc.right{left:144px}
.toc-item{position:relative;height:37.6px;border-bottom:1px solid var(--rule);width:122px}
.toc-num{position:absolute;left:0;top:6px;width:11px;height:17px;background:var(--ink);color:#fff;font-size:11px;text-align:center;line-height:17px}
.toc-label{position:absolute;left:15px;top:9px;font-size:8.5px;line-height:1.3;width:78px}
.toc-page{position:absolute;right:0;top:3px;font-size:14px;font-weight:300}
/* about */
.h-page{font-size:19px;font-weight:400;letter-spacing:.3px}
.pull{border:1px solid var(--ink);font-size:10.5px;line-height:1.25;padding:4px 8px}
/* locations */
.caption{font-weight:300;color:var(--ink)}
.bonus{border:1px solid var(--ink)}
/* neighbourhood */
.item-title{font-size:14px;font-weight:300}
.item-title b{font-weight:300;font-size:17px;margin-right:4px}
.tag{color:#fff;font-weight:300}
.tag.blue{background:var(--blue);font-size:15px;padding:3px 8px}
.tag.magenta{background:var(--magenta);font-size:12px;line-height:1.3;padding:4px 6px}
.tag.yellow{background:var(--yellow);font-size:9px;line-height:1.3;padding:5px 7px}
.spread-title{font-size:31px;font-weight:300;line-height:1.1;white-space:nowrap;top:142px}
.photo-num{position:absolute;color:#fff;font-size:18px;font-weight:300}
.big-title{font-size:35px;font-weight:300;line-height:1.05}
.bar{background:var(--blue)}
</style>
</head>
<body>

<!-- Contents -->
<section class="page row-top p1">
  <span class="folio" style="right:10px;top:10px">1</span>
  <h1 class="abs contents-title">Contents</h1>
  <div class="toc left">
    <div class="toc-item"><span class="toc-num">1</span><span class="toc-label">About Lumiveso</span><span class="toc-page">2</span></div>
    <div class="toc-item"><span class="toc-num">2</span><span class="toc-label">Prime Location</span><span class="toc-page">4</span></div>
    <div class="toc-item"><span class="toc-num">3</span><span class="toc-label">What to see in the Neighbour Hood?</span><span class="toc-page">6</span></div>
    <div class="toc-item"><span class="toc-num">4</span><span class="toc-label">Better look of Lumiveso</span><span class="toc-page">8</span></div>
    <div class="toc-item"><span class="toc-num">5</span><span class="toc-label">Arabic Courses</span><span class="toc-page">10</span></div>
    <div class="toc-item"><span class="toc-num">6</span><span class="toc-label">About Courses</span><span class="toc-page">12</span></div>
    <div class="toc-item"><span class="toc-num">7</span><span class="toc-label">General Arabic</span><span class="toc-page">14</span></div>
  </div>
  <div class="toc right">
    <div class="toc-item"><span class="toc-num">8</span><span class="toc-label">Tunisian Arabic</span><span class="toc-page">16</span></div>
    <div class="toc-item"><span class="toc-num">9</span><span class="toc-label">Afternoon Seminars</span><span class="toc-page">18</span></div>
    <div class="toc-item"><span class="toc-num">10</span><span class="toc-label">Accommodation</span><span class="toc-page">20</span></div>
    <div class="toc-item"><span class="toc-num">11</span><span class="toc-label">Flat Share</span><span class="toc-page">22</span></div>
    <div class="toc-item"><span class="toc-num">12</span><span class="toc-label">Hotel</span><span class="toc-page">24</span></div>
    <div class="toc-item"><span class="toc-num">13</span><span class="toc-label">Homestay</span><span class="toc-page">26</span></div>
    <div class="toc-item"><span class="toc-num">14</span><span class="toc-label">Weekend Trips in Tunisia</span><span class="toc-page">28</span></div>
  </div>
</section>

<!-- About -->
<section class="page row-top p2">
  <div class="photo night" style="left:0;top:0;width:283px;height:205px" role="img" aria-label="City at night with a lit clock tower and palm-lined avenue"></div>
  <h2 class="abs h-page" style="left:16px;top:220px">About Lumiveso</h2>
  <div class="abs small" style="left:16px;top:250px;width:116px">
    <p>Sed ut perspiciatis unde omnis iste natus error sit voluptatem accusantium doloremque laudantium, totam rem aperiam, eaque ipsa quae ab illo inventore veritatis et quasi architecto beatae vitae dicta sunt explicabo.</p>
    <p style="margin-top:6px">Nemo enim ipsam voluptatem quia voluptas sit aspernatur aut odit aut fugit, sed quia consequuntur magni dolores eos qui ratione voluptatem sequi nesciunt. Neque porro quisquam est, qui dolo</p>
  </div>
  <div class="abs small" style="left:145px;top:250px;width:122px">
    <p>Lorem quia dolor sit amet, consectetur, adipisci velit, sed quia non numquam eius modi tempora incidunt ut labore et dolore magnam aliquam quaerat voluptatem.</p>
  </div>
  <div class="abs pull" style="left:145px;top:296px;width:122px">dignissimos ducmus qui blandit il praesentium voluptatum deleniti</div>
</section>

<!-- Locations -->
<section class="page row-top p3">
  <span class="folio" style="left:8px;top:8px">3</span>
  <h2 class="abs h-page" style="left:16px;top:18px">Locations</h2>
  <div class="abs small" style="left:16px;top:48px;width:92px">
    <p>Atvero eos et accusamus et iusto odio dignissimos ducimus qui blanditiis praesentium voluptatum deleniti atque corrupti quos dolores et quas molestias excepturi sint occaecati cupiditate non provident, similique qui officia</p>
    <p style="margin-top:6px">Atvero eos et accusamus et iusto odio dignissimos ducimus qui</p>
    <p class="bold" style="margin-top:6px">bccusamus et iusto odio dignis imos ducimus qui blanditiis</p>
  </div>
  <div class="photo church" style="left:114px;top:16px;width:152px;height:156px" role="img" aria-label="Cathedral facade with twin towers under blue sky"></div>
  <div class="photo" style="left:16px;top:183px;width:251px;height:167px;background:var(--map)" role="img" aria-label="Map of the region with marked school locations"></div>
</section>

<!-- Prime location -->
<section class="page row-top p4">
  <div class="photo whitetown" style="left:16px;top:16px;width:116px;height:128px" role="img" aria-label="White house with blue door and palm trees"></div>
  <h3 class="abs caption" style="left:16px;top:150px;font-size:13.5px">Atvero eos et acmus</h3>
  <p class="abs small" style="left:16px;top:170px;width:122px">Cupiditate non provident, similique sunt in culpa qui officia deserunt mollitia animi, id est laborum et dolorum fuga.</p>
  <div class="photo ruins" style="left:152px;top:30px;width:116px;height:128px" role="img" aria-label="Ancient amphitheatre ruins"></div>
  <h3 class="abs caption" style="left:152px;top:164px;font-size:13.5px">Etiusto odio dignis</h3>
  <p class="abs small" style="left:152px;top:184px;width:118px">Cupiditate non provident, similique sunt in culpa qui officia deserunt mollitia animi, id est laborum et dolorum fuga.</p>
  <div class="photo roofs" style="left:16px;top:222px;width:76px;height:54px" role="img" aria-label="Rooftops of the old town"></div>
  <h3 class="abs caption" style="left:16px;top:280px;font-size:9.5px">Rerum nece ssitati</h3>
  <p class="abs small" style="left:16px;top:295px;width:78px;font-size:5.5px">Cupiditate non provident, sim ilique sunt in culpa qui officia deserunt mollitia animi, id est laborum et dolorum fuga.</p>
  <div class="photo harbour" style="left:104px;top:238px;width:76px;height:56px" role="img" aria-label="Harbour with boats and city skyline"></div>
  <h3 class="abs caption" style="left:104px;top:299px;font-size:9.5px">Voluptates repudian</h3>
  <p class="abs small" style="left:104px;top:314px;width:76px;font-size:5.5px">culpa qui officia deserunt molli tia animi, id est laborum et</p>
  <div class="abs bonus" style="left:191px;top:227px;width:76px;height:110px">
    <span class="abs caption" style="left:5px;top:4px;font-size:9px">Bonus entry</span>
    <div class="photo roofs" style="left:5px;top:22px;width:64px;height:44px" role="img" aria-label="View over the medina rooftops"></div>
    <p class="abs small" style="left:5px;top:72px;width:66px;font-size:5.5px">culpa qui officia deserunt molli tia animi, id est labo rum et officia dese</p>
  </div>
  <span class="folio" style="left:10px;top:354px">4</span>
</section>

<!-- Neighbourhood left -->
<section class="page row-bottom p5">
  <h3 class="abs item-title" style="left:18px;top:20px"><b>1</b>Atveroeos etacmus</h3>
  <p class="abs small" style="left:32px;top:40px;width:132px">Cupiditate non provident, similique sunt in culpa qui officia deserunt mollitia animi, id est laborum et dolorum fuga.</p>
  <span class="abs tag blue" style="left:14px;top:69px">BEST IN THE TOWN</span>
  <h3 class="abs item-title" style="left:18px;top:108px"><b>2</b>Dignissimos zucimus</h3>
  <p class="abs small" style="left:32px;top:129px;width:122px">aesentium voluptatum deleniti atque corrupti quos dolores et quas molestias</p>
  <p class="abs small bold" style="left:32px;top:151px;width:122px">excepturi sint occaecati cupiditate non provident, similique</p>
  <span class="abs tag magenta" style="left:30px;top:173px;width:140px">Aesentium voluptati dele niti atque corie upti quos dolores et quas</span>
  <h3 class="abs item-title" style="left:18px;top:232px"><b>3</b>Ducimus qui blanf</h3>
  <p class="abs small" style="left:32px;top:253px;width:104px">aesentium voluptatum deleniti atque corrupti quos dolores et quas molestias pti quos dolo</p>
  <h3 class="abs item-title" style="left:144px;top:230px"><b>4</b>Namlibero temp</h3>
  <p class="abs small" style="left:158px;top:252px;width:84px">placeat facere possimus, omnis voluptas assumenda est, omnis dolor repellendus. Temporibus autem quibusdam et aut officiis debitis aut rerum</p>
  <span class="abs tag yellow" style="left:144px;top:295px;width:94px">facere possimus, il voluptas assumend est, omnis dolor</span>
  <h3 class="abs item-title" style="left:26px;top:292px"><b>5</b>Vamsoluta nobis</h3>
  <p class="abs small" style="left:42px;top:313px;width:104px">s saepe eveniet ut et voluptates repudiandae sint et molestiae non recusandae. Itaque earum tet molestiae non recusanda</p>
  <div class="photo whitetown" style="left:158px;top:17px;width:127px;height:120px" role="img" aria-label="Whitewashed village with blue shutters"></div>
  <div class="photo waterfall" style="left:250px;top:205px;width:35px;height:146px" role="img" aria-label="Waterfall in a rocky oasis"></div>
  <span class="photo-num" style="left:256px;top:326px">5</span>
  <h2 class="abs spread-title" style="left:185px">What to see in the<br>Neighbour Hood?</h2>
</section>

<!-- Neighbourhood right -->
<section class="page row-bottom p6">
  <div class="photo whitetown" style="left:0;top:17px;width:104px;height:120px" role="img" aria-label="Whitewashed village street"></div>
  <span class="photo-num" style="left:88px;top:20px">1</span>
  <div class="photo roofs" style="left:114px;top:17px;width:153px;height:140px" role="img" aria-label="Old town rooftops and domes"></div>
  <span class="photo-num" style="left:119px;top:20px">2</span>
  <div class="photo church" style="left:114px;top:166px;width:153px;height:90px" role="img" aria-label="Cathedral towers with palm fronds"></div>
  <span class="photo-num" style="left:119px;top:198px">3</span>
  <div class="photo harbour" style="left:114px;top:267px;width:153px;height:83px" role="img" aria-label="Harbour and breakwater"></div>
  <span class="photo-num" style="left:251px;top:326px">4</span>
  <div class="photo waterfall" style="left:0;top:205px;width:104px;height:146px" role="img" aria-label="Waterfall pool among rocks"></div>
  <span class="abs spread-title" style="left:-110px" aria-hidden="true">What to see in the<br>Neighbour Hood?</span>
</section>

<!-- Better look left -->
<section class="page row-bottom p7">
  <div class="photo night" style="left:24px;top:0;width:258px;height:269px" role="img" aria-label="Clock tower and boulevard lit at night"></div>
  <h2 class="abs big-title" style="left:24px;top:276px">Better look of<br>Lumiveso</h2>
  <div class="abs bar" style="left:264px;top:282px;width:18px;height:65px"></div>
</section>

<!-- Better look right -->
<section class="page row-bottom p8">
  <div class="photo night" style="left:0;top:0;width:261px;height:269px" role="img" aria-label="Hotel facades and palm trees at night"></div>
  <div class="abs bar" style="left:0;top:282px;width:21px;height:65px"></div>
  <p class="abs small bold" style="right:24px;top:278px;width:210px;text-align:right;font-size:7px">placeat facere possimus, omnis voluptas assumenda est, omnis dolor repellendus. Temporibus autem quibusdam et aut officiis debitis aut rerum</p>
  <p class="abs small" style="right:24px;top:314px;width:210px;text-align:right;font-size:7px">sint occaecati cupiditate non provident, similique sunt in culpa qui officia deserunt mollitia animi, id est laborum et dolorum fuga. Et harum , id est laborum et doloru</p>
</section>

</body>
</html>
```